Wine Shop Banners

Banner graphic/images required
Require banner images to match the present online wine shop.

www.kelterhaus-traube.de

The wine-shop presently has a very clean, simple design, lots of white space, which is very much the trend at the moment.

Requirements
Images or graphic design for present banners visible on the homepage

The colour and feeling of the banners must fit in with the present clean, simple design.

Work required
3 large slide-card/banners (can be more) and 3 smaller fixed banners below. Please view website to see present position of banners.

LARGE BANNERS x 3

Something special with white background within the banner space
White background on each slide-card. Small individual graphic image in the middle of the slide card. This could be either a simple element of wine:
ingredients, fruit (grape), bottle, cork, old bottle label etc. just displaying one item on each slide-card. Preferably with high quality graphic features.

Note:
We are trying the steer away from the classic stereotype wineshop design. The image/s should have a higher, individual graphic touch, which gives the design something different. Sometimes such artistic work is displayed in steampunk or even in nostalgic design, which leaves the viewer slightly memorized with the content.
To clarify: we are not looking for a full steampunk design but possibly certain elements of this will give you an idea what we mean. That is to say, the design can go slightly in this direction without going over the top. Something small but very eye-catching.

SMALLER BANNERS x 3

One idea is:
Showing a symbol e.g. - discount sign "%" against a white background but again with a high graphic quality.

Target Market(s)

People interested in purchasing wine.
Ages approx. 25 to 65

Industry/Entity Type

Shop

Requirements
Must have
• Something special with white background
• Small individual graphic image in the middle of the slide card.
Nice to have
• The image/s should have a higher, individual graphic touch, which gives the design something different. Something that leaves the viewer slightly memorized with the content.
Should not have
• Not the typical classical design that is often seen on wine shops.

```html
<!DOCTYPE html>
<html lang="de">
<head>
<meta charset="utf-8">
<title>Kelterhaus Traube – Weinshop</title>
<link href="https://fonts.googleapis.com/css2?family=Exo+2:wght@300;400&family=Great+Vibes&family=Cormorant+Garamond:ital,wght@0,500;1,400;1,500&display=swap" rel="stylesheet">
<style>
:root{
  --wine:#b8194a;
  --olive:#4d5a2a;
  --lime:#cdd962;
  --lime-text:#c7d255;
  --ink:#444;
  --muted:#9a9a9a;
  --line:#e4e4e4;
  --beige:#c9b899;
  --taupe:#7a6a58;
  --purple:#6a2b8c;
}
*{margin:0;padding:0;box-sizing:border-box}
html,body{width:1200px;height:749px;overflow:hidden;background:#fff}
body{position:relative;font-family:"Exo 2",sans-serif;font-weight:300;color:var(--ink)}
.abs{position:absolute}

.brand{left:34px;top:40px;width:190px}
.brand-name{font-family:"Exo 2",sans-serif;font-weight:400;font-size:34px;color:var(--olive);letter-spacing:1px;line-height:1}
.brand-sub{font-family:"Exo 2",sans-serif;font-weight:400;font-size:13px;color:var(--olive);letter-spacing:8px;margin-top:10px}

.search{left:592px;top:52px;width:314px;height:36px;border:1px solid #9a9a9a;display:flex}
.search svg{margin:10px 12px 0 12px}
.search-input{flex:1;font-size:15px;color:#777;line-height:34px}
.search-go{width:46px;background:var(--wine);color:#fff;font-size:16px;text-align:center;line-height:34px;font-weight:400}

.account{left:1011px;top:40px;font-size:18px;color:#555;display:flex;gap:14px;align-items:center}

.nav{left:52px;top:137px;display:flex;gap:0;font-size:19px;color:#555}
.nav span{position:absolute;white-space:nowrap}
.badge{position:absolute;width:17px;height:17px;border-radius:50%;background:#b6b82e;color:#fff;font-size:11px;text-align:center;line-height:17px;font-weight:400}

.sidebar{left:33px;top:180px;width:233px}
.filter-head{height:39px;background:var(--lime);color:var(--olive);font-size:17px;font-weight:400;padding:9px 13px}
.group-title{position:absolute;left:3px;font-size:16px;font-weight:400;color:var(--lime-text)}
.facet{position:absolute;left:4px;font-size:17px;color:#555;white-space:nowrap}
.facet::before{content:"›";margin-right:9px;color:#555}
.facet em{font-style:normal;color:var(--muted)}
.scroll{left:250px;top:266px;width:13px;height:182px;background:#eee}
.scroll i{position:absolute;left:1px;top:12px;width:11px;height:82px;background:#bbb}

.hero{left:279px;top:179px;width:867px;height:341px;background:#fff;box-shadow:0 0 4px rgba(0,0,0,.15);overflow:hidden}
.hero-photo{position:absolute;right:0;top:0;width:520px;height:341px;background:radial-gradient(ellipse at 55% 55%,#4a4a72 0%,#5c5678 40%,#8b84a0 62%,rgba(255,255,255,0) 78%),linear-gradient(200deg,#7cae3a 0%,rgba(255,255,255,0) 30%)}
.hero-title{position:absolute;left:66px;top:86px;font-family:"Great Vibes",cursive;font-size:76px;line-height:64px;color:var(--wine)}
.hero-title span{display:block;padding-left:44px}
.hero-tag{position:absolute;left:26px;top:300px;font-family:"Cormorant Garamond",serif;font-style:italic;font-size:19px;color:#222}
.dots{position:absolute;left:775px;top:301px;display:flex;gap:11px}
.dots i{width:19px;height:19px;border-radius:50%;background:#fff;box-shadow:0 0 3px rgba(0,0,0,.35)}
.dots i:first-child{background:var(--purple)}

.promo{top:529px;width:282px;height:134px;background:linear-gradient(90deg,#e6e6e6,#f7f7f7);box-shadow:0 1px 3px rgba(0,0,0,.2);overflow:hidden;font-family:"Cormorant Garamond",serif;font-style:italic}
.promo-band{position:absolute;top:0;right:0;height:134px}
.promo-copy{position:absolute;color:var(--taupe)}
.promo-play{position:absolute;right:7px;bottom:7px}

.section-head{left:277px;top:686px;display:flex;gap:10px;align-items:center;font-family:"Cormorant Garamond",serif;font-weight:500;font-size:21px;color:#222}
.pager{top:685px;width:19px;height:20px;border:1px solid #777}
.rule{left:273px;top:716px;width:878px;height:4px;background:#eee}
.card-edge{top:720px;width:216px;height:10px;border-left:1px solid var(--line);border-right:1px solid var(--line)}
</style>
</head>
<body>

<div class="abs brand">
  <div class="brand-name">KELTERHAUS</div>
  <div class="brand-sub">TRAUBE</div>
</div>

<div class="abs search">
  <svg width="16" height="16" viewBox="0 0 16 16"><circle cx="6.5" cy="6.5" r="4.8" fill="none" stroke="#b8194a" stroke-width="2.2"/><line x1="10" y1="10" x2="14" y2="14" stroke="#b8194a" stroke-width="2.4"/></svg>
  <div class="search-input">Suche</div>
  <div class="search-go">GO</div>
</div>

<div class="abs account">Abmelden
  <svg width="26" height="30" viewBox="0 0 26 30"><circle cx="13" cy="8" r="6" fill="none" stroke="#555" stroke-width="1.8"/><path d="M2 28v-4c0-4 4-7 11-7s11 3 11 7v4z" fill="none" stroke="#555" stroke-width="1.8"/></svg>
</div>

<nav class="abs nav">
  <span style="left:0">Rotwein</span>
  <span style="left:108px">Weißwein</span>
  <span style="left:231px">Rosewein</span>
  <span style="left:351px">Sekt / Champagner</span>
  <span style="left:553px">Sonderangebote</span>
  <span style="left:734px">Probierpakete</span>
</nav>

<div class="abs" style="left:1046px;top:132px">
  <svg width="30" height="28" viewBox="0 0 30 28"><path d="M1 3h5l4 15h15l3-10H8" fill="none" stroke="#777" stroke-width="2"/><circle cx="12" cy="23" r="2" fill="#777"/><circle cx="23" cy="23" r="2" fill="#777"/></svg>
  <div class="badge" style="left:22px;top:-6px">0</div>
</div>
<div class="abs" style="left:1106px;top:132px">
  <svg width="34" height="34" viewBox="0 0 34 34"><circle cx="17" cy="17" r="17" fill="#8a8a8a"/><path d="M17 24l-7-7a4 4 0 0 1 7-4 4 4 0 0 1 7 4z" fill="none" stroke="#fff" stroke-width="1.8"/></svg>
  <div class="badge" style="left:25px;top:-6px">0</div>
</div>

<aside class="abs sidebar">
  <div class="filter-head">DETAILSUCHE</div>
</aside>
<div class="abs" style="left:33px;top:0">
  <div class="group-title" style="top:235px">LAND</div>
  <div class="facet" style="top:267px">Italien <em>(87)</em></div>
  <div class="facet" style="top:292px">Frankreich <em>(74)</em></div>
  <div class="facet" style="top:317px">Deutschland <em>(58)</em></div>
  <div class="facet" style="top:342px">Spanien <em>(35)</em></div>
  <div class="facet" style="top:367px">Südafrika <em>(15)</em></div>
  <div class="facet" style="top:392px">Österreich <em>(12)</em></div>
  <div class="facet" style="top:417px">Australien <em>(12)</em></div>
  <div class="group-title" style="top:471px">GESCHMACK</div>
  <div class="facet" style="top:505px">Trocken <em>(303)</em></div>
  <div class="facet" style="top:530px">Halbtrocken <em>(8)</em></div>
  <div class="facet" style="top:555px">Lieblich <em>(5)</em></div>
  <div class="facet" style="top:580px">Süß <em>(3)</em></div>
  <div class="facet" style="top:605px">Edelsüss <em>(1)</em></div>
  <div class="group-title" style="top:650px">FARBE</div>
  <div class="facet" style="top:684px">Rot <em>(155)</em></div>
  <div class="facet" style="top:709px">Weiß <em>(127)</em></div>
</div>
<div class="abs scroll"><i></i></div>

<section class="abs hero">
  <div class="hero-photo" role="img" aria-label="Bunch of dark red grapes with a green vine leaf"></div>
  <div class="hero-title">The Finest<span>Red Wine</span></div>
  <div class="hero-tag">The Perfect Gift Anytime</div>
  <div class="dots"><i></i><i></i><i></i></div>
</section>

<div class="abs promo" style="left:278px">
  <svg class="promo-band" width="180" height="134" viewBox="0 0 180 134"><polygon points="80,0 180,0 180,134 0,134" fill="#c9b899"/></svg>
  <div class="promo-copy" style="left:26px;top:22px;font-size:27px;line-height:29px">free shipping<br>on orders<br>over</div>
  <div class="promo-copy" style="left:158px;top:38px;font-size:72px;color:#fff;font-style:normal;font-weight:500;line-height:1">$25</div>
  <svg class="promo-play" width="22" height="22" viewBox="0 0 22 22"><circle cx="11" cy="11" r="10" fill="#fff"/><polygon points="8,6 16,11 8,16" fill="#c9b899"/></svg>
</div>

<div class="abs promo" style="left:571px">
  <div class="abs" role="img" aria-label="Cork popping out with a splash of sparkling wine" style="left:0;top:0;width:170px;height:134px;background:radial-gradient(ellipse at 45% 45%,#b8a48a,#e6e0d6 60%,#f4f4f4)"></div>
  <svg class="promo-band" width="180" height="134" viewBox="0 0 180 134"><polygon points="80,0 180,0 180,134 0,134" fill="#7a6a58"/></svg>
  <div class="promo-copy" style="left:155px;top:48px;font-size:34px;line-height:28px;color:#fff">celebrate<br>in style</div>
  <svg class="promo-play" width="22" height="22" viewBox="0 0 22 22"><circle cx="11" cy="11" r="10" fill="#fff"/><polygon points="8,6 16,11 8,16" fill="#7a6a58"/></svg>
</div>

<div class="abs promo" style="left:864px">
  <svg class="promo-band" width="180" height="134" viewBox="0 0 180 134"><polygon points="80,0 180,0 180,134 0,134" fill="#7a6a58"/></svg>
  <div class="promo-copy" style="left:26px;top:38px;font-size:40px;line-height:30px">special<br>offers</div>
  <div class="promo-copy" style="left:170px;top:24px;font-size:22px;color:#fff">save up to</div>
  <div class="promo-copy" style="left:148px;top:44px;font-size:72px;color:#fff;line-height:1">35%</div>
  <svg class="promo-play" width="22" height="22" viewBox="0 0 22 22"><circle cx="11" cy="11" r="10" fill="#fff"/><polygon points="8,6 16,11 8,16" fill="#7a6a58"/></svg>
</div>

<div class="abs section-head">
  <svg width="19" height="19" viewBox="0 0 19 19"><circle cx="9.5" cy="9.5" r="8.5" fill="none" stroke="#b8194a" stroke-width="1.4"/><polygon points="7.5,5.5 13,9.5 7.5,13.5" fill="#b8194a"/></svg>
  Ausgewählte Produkte
</div>
<svg class="abs pager" style="left:1102px" viewBox="0 0 19 20"><polyline points="11,5 6,10 11,15" fill="none" stroke="#555" stroke-width="1.4"/></svg>
<svg class="abs pager" style="left:1126px" viewBox="0 0 19 20"><polyline points="8,5 13,10 8,15" fill="none" stroke="#555" stroke-width="1.4"/></svg>
<div class="abs rule"></div>
<div class="abs card-edge" style="left:274px"></div>
<div class="abs card-edge" style="left:494px"></div>
<div class="abs card-edge" style="left:713px"></div>
<div class="abs card-edge" style="left:933px"></div>

</body>
</html>
```